Startup online payment business - Sporting / Golf, Swift Tee payment

Background:
Our business name is "Swift Tee" we provide online payments for golfing services via our website. We currently have a logo used on our website. No other design style has been developed. Our aim is to remove cash payments for service at golf clubs.

Our Key Values:
Quick and easy
Formal and polite
Fun with professional boundary
Mate-ship relationships
100% online digital

What we want from you:
Marketing design to be used on posters and stickers in a retail setting to direct customers to our online payment Chanel.
Design must incorporate attached logo, URL swifttee.com.au and our key values can act as a guide the type of design. We have used color Hex#007672 for logo background. We are open to use other colors.

Target Market(s)

Golf clubs and golf players

Industry/Entity Type

Golf Course

Font styles to use
Sans Serif

Requirements
Must have
• Directions to online payment via URL: swifttee.com.au
Nice to have
• We like the idea of the slogan: No Cash - No worries. Have attached home screen that will be available from URL link. Consideration if using mobile phone in image. Push the online payment and steps 1. Visit swifttee.com 2. Select club 3. Confirm payment
Should not have
• Cartoons

```html
<!DOCTYPE html>
<html lang="en">
<head>
<meta charset="utf-8">
<title>Swift Tee – Poster</title>
<link rel="stylesheet" href="https://fonts.googleapis.com/css2?family=Montserrat:wght@300;500;600;700&display=swap">
<style>
  :root {
    --backdrop: #b5c4c2;
    --green-deep: #1b9465;
    --green-mid: #35c983;
    --green-mint: #6fffc4;
    --forest: #0e4a32;
    --navy: #2a3a52;
    --white: #ffffff;
    --phone-light: #eef1f3;
  }
  * { margin: 0; padding: 0; box-sizing: border-box; }
  html, body { width: 1200px; height: 1200px; overflow: hidden; }
  body {
    background: var(--backdrop);
    font-family: "Montserrat", sans-serif;
    position: relative;
  }
  .poster {
    position: absolute;
    left: 0; top: 190px;
    width: 1200px; height: 820px;
    background: var(--green-deep);
    overflow: hidden;
  }
  .poster-waves { position: absolute; inset: 0; width: 100%; height: 100%; }
  .brand-name {
    position: absolute;
    left: 42px; top: 60px;
    width: 402px;
    color: var(--white);
    font-weight: 700;
    font-size: 96px;
    line-height: 1;
    letter-spacing: 4px;
    text-align: center;
    text-transform: uppercase;
  }
  .tagline {
    position: absolute;
    left: 40px; top: 276px;
    width: 606px;
    color: var(--white);
    font-weight: 300;
    font-size: 30px;
    line-height: 35px;
    text-align: center;
  }
  .steps { position: absolute; left: 710px; top: 79px; list-style: none; }
  .step {
    position: relative;
    width: 252px; height: 52px;
    margin-bottom: 27px;
  }
  .step-bar {
    position: absolute;
    left: 26px; top: 14px;
    width: 224px; height: 24px;
    background: var(--navy);
    border-radius: 0 8px 8px 0;
    color: var(--white);
    font-weight: 600;
    font-size: 18px;
    line-height: 24px;
    padding-left: 35px;
    white-space: nowrap;
  }
  .step-number {
    position: absolute;
    left: 0; top: 0;
    width: 52px; height: 52px;
    border-radius: 50%;
    background: var(--green-mint);
    color: var(--forest);
    font-weight: 700;
    font-size: 32px;
    line-height: 52px;
    text-align: center;
  }
  .app-preview {
    position: absolute;
    left: 999px; top: 26px;
    width: 161px; height: 320px;
    border-radius: 22px;
    background: linear-gradient(180deg, var(--phone-light) 0%, var(--green-deep) 18%, var(--green-deep) 82%, var(--phone-light) 100%);
  }
  .slogan {
    position: absolute;
    left: 1022px; top: 352px;
    list-style: none;
    color: var(--navy);
    font-weight: 500;
    font-size: 21px;
    line-height: 24px;
  }
  .slogan li::before { content: "\2713"; margin-right: 6px; font-size: 17px; }
  .values { position: absolute; left: 41px; top: 439px; list-style: none; }
  .value-card {
    position: absolute;
    top: 0;
    width: 170px; height: 215px;
    border-radius: 28px;
    background: var(--forest);
    color: var(--white);
    font-weight: 600;
    display: flex; align-items: center; justify-content: center;
    text-align: center;
    padding-bottom: 20px;
  }
  .value-card::before {
    content: "";
    position: absolute;
    top: 0; left: 65px;
    width: 40px; height: 20px;
    border-radius: 0 0 20px 20px;
    background: var(--green-mint);
  }
  .value-card.large { font-size: 31px; line-height: 34px; }
  .value-card.small { font-size: 23px; line-height: 34px; }
  .site-url {
    position: absolute;
    right: 40px; top: 745px;
    color: var(--forest);
    font-weight: 700;
    font-size: 44px;
    line-height: 50px;
  }
</style>
</head>
<body>
  <main class="poster">
    <svg class="poster-waves" viewBox="0 0 1734 1185" preserveAspectRatio="none" aria-hidden="true">
      <path fill="var(--green-mid)" d="M0,1185 C80,950 250,720 540,610 C720,560 900,550 1100,500 C1400,420 1600,320 1734,235 L1734,1185 Z"/>
      <path fill="var(--green-mint)" d="M940,1185 C1050,1060 1200,990 1340,988 C1560,985 1690,900 1734,800 L1734,1185 Z"/>
    </svg>

    <h1 class="brand-name">Swift<br>Tee</h1>

    <p class="tagline">Swift Tee is here to support Golf Clubs embrace new strategies for success in a rapidly changing world.</p>

    <ol class="steps">
      <li class="step"><span class="step-bar">Visit swifttee.com</span><span class="step-number">1</span></li>
      <li class="step"><span class="step-bar">Select club</span><span class="step-number">2</span></li>
      <li class="step"><span class="step-bar">Confirm payment</span><span class="step-number">3</span></li>
    </ol>

    <div class="app-preview" role="img" aria-label="Mobile phone showing the Swift Tee payment home screen"></div>

    <ul class="slogan">
      <li>No Cash</li>
      <li>No worries</li>
    </ul>

    <ul class="values">
      <li class="value-card large" style="left:0">Quick<br>and<br>Easy</li>
      <li class="value-card large" style="left:194px">Formal<br>and<br>Polite</li>
      <li class="value-card small" style="left:389px">Fun with<br>professional<br>boundary</li>
      <li class="value-card small" style="left:587px">Mate-ship<br>relationships</li>
      <li class="value-card large" style="left:785px">100%<br>online<br>digital</li>
    </ul>

    <p class="site-url">swifttee.com.au</p>
  </main>
</body>
</html>
```